New PowerPoint Design Project

A well-known speaker needs a visual presence that compliments his amazing, consistent performance onstage. You'll easily improve this deck, and I'll leave it to you whether you stick with the palette defined by the original BLQEMS icons you'll find in the deck, the mishmosh in the deck as it stands, OR get extra points by going with the corporate color palette so our speaking slides fit with Ronan's brands and his three sub-brands. A look at the Ronan subbrand .png in the attached zip file might give you some ideas.
Updates

Just noting that I'm available to answer questions or supply assets you think you'd need. The big design issue I'm looking for someone to solve is how you'll treat the bright clusters of icons in information graphics of the deck.

Target Market(s)

Corporate Executives and wanabees

Requirements
Must have
• The footer needs to have the Dellwyn Bluepath logo and Twitter and Facebook link and you need to do the first 27 slides. The slides past 27 are there simply if you want to use assets from those slides.
Nice to have
• Use the palette document in the zip rather than palette dictated by the BLQEMS icons in the deck (I do not have source for the icons.).

```html
<!DOCTYPE html>
<html lang="en">
<head>
<meta charset="utf-8">
<title>Project Title Here</title>
<link rel="stylesheet" href="https://fonts.googleapis.com/css2?family=Open+Sans:wght@400;600;700&family=Archivo+Black&display=swap">
<style>
  :root {
    --ink: #0d0b0b;
    --white: #ffffff;
    --text-grey: #6a6a6a;
    --relational-green: #3a8f1c;
    --collab-orange: #ff4a12;
    --field-green: #5fe22a;
    --field-light: #b8f57a;
    --field-deep: #33b214;
    --brand-green: #7fa83a;
    --social-blue: #2c7fd0;
    --haze: #ececec;
  }
  * { box-sizing: border-box; margin: 0; padding: 0; }
  html, body { width: 1200px; height: 900px; overflow: hidden; }
  body { background: var(--white); font-family: "Open Sans", Arial, sans-serif; }
  .slide { position: relative; width: 1200px; height: 900px; overflow: hidden; background: var(--white); }

  .slide-header {
    position: absolute; left: 0; top: 0; width: 1200px; height: 108px;
    background: var(--ink);
  }
  .slide-title {
    position: absolute; left: 27px; top: 22px;
    color: var(--white); font-size: 49px; font-weight: 400; letter-spacing: 0.5px; line-height: 1;
  }
  .header-haze {
    position: absolute; left: 0; top: 108px; width: 1200px; height: 110px;
    background: linear-gradient(to bottom, var(--haze), rgba(255,255,255,0));
  }
  .backdrop-texture {
    position: absolute; left: 0; top: 200px; width: 560px; height: 620px;
    background: radial-gradient(ellipse at 0% 55%, rgba(200,200,200,0.45), rgba(255,255,255,0) 70%);
  }

  .focus-copy { position: absolute; left: 30px; top: 150px; }
  .focus-lead {
    color: var(--text-grey); font-weight: 600; font-size: 31px; line-height: 55px; letter-spacing: 1.5px;
  }
  .focus-key {
    font-weight: 700; font-size: 45px; line-height: 64px; letter-spacing: 1.5px; margin-top: 8px;
  }
  .focus-key .relational { color: var(--relational-green); }
  .focus-key .joiner { color: var(--text-grey); }
  .focus-key .collaborative { color: var(--collab-orange); }

  .chain-panel {
    position: absolute; left: 438px; top: 156px; width: 732px; height: 545px;
    border: 2px solid var(--ink);
    background:
      radial-gradient(circle at 30% 75%, rgba(40,150,10,0.55), rgba(40,150,10,0) 30%),
      radial-gradient(circle at 75% 30%, var(--field-light), rgba(184,245,122,0) 35%),
      radial-gradient(circle at 55% 70%, rgba(184,245,122,0.8), rgba(184,245,122,0) 30%),
      linear-gradient(135deg, var(--field-green), var(--field-deep) 55%, var(--field-green));
  }
  .chain-row {
    position: absolute; left: 0; width: 100%; height: 80px;
    font-family: "Archivo Black", "Arial Black", sans-serif; font-size: 60px; color: var(--ink); line-height: 80px;
  }
  .chain-row span { position: absolute; top: 0; white-space: nowrap; }
  .chain-row .node-x { left: 44px; }
  .chain-row .arrow-a { left: 120px; letter-spacing: 10px; }
  .chain-row .node-y { left: 334px; }
  .chain-row .arrow-b { left: 410px; letter-spacing: 10px; }
  .chain-row .node-p { left: 630px; }

  .slide-footer {
    position: absolute; left: 0; top: 828px; width: 1200px; height: 72px; background: var(--ink);
  }
  .brand-mark {
    position: absolute; left: 14px; top: 816px; width: 58px; height: 58px;
    background: var(--brand-green); border: 3px solid var(--white);
  }
  .brand-name {
    position: absolute; left: 92px; top: 836px;
    color: var(--brand-green); font-size: 37px; font-weight: 400; line-height: 1;
  }
  .social { position: absolute; top: 842px; height: 40px; display: flex; align-items: center; white-space: nowrap; }
  .social-dot { width: 40px; height: 40px; border-radius: 50%; background: var(--social-blue); margin-right: 9px; flex: none; }
  .social-handle { color: var(--white); font-size: 17px; }
  .social-chirp { left: 868px; }
  .social-page { left: 1018px; }
</style>
</head>
<body>
<div class="slide">
  <header class="slide-header"><h1 class="slide-title">PROJECT TITLE HERE</h1></header>
  <div class="header-haze"></div>
  <div class="backdrop-texture" role="img" aria-label="Faint grey dot pattern fading across the background"></div>

  <div class="focus-copy">
    <p class="focus-lead">Focus on<br>Highest return<br>behaviors:</p>
    <p class="focus-key"><span class="relational">Relational</span> <span class="joiner">and</span><br><span class="collaborative">collaborative</span></p>
  </div>

  <div class="chain-panel" role="img" aria-label="Blurred bright green bokeh backdrop with behavior chains">
    <div class="chain-row" style="top:22px"><span class="node-x">X</span><span class="arrow-a">----&gt;</span><span class="node-y">Y</span><span class="arrow-b">----&gt;</span><span class="node-p">P</span></div>
    <div class="chain-row" style="top:119px"><span class="node-x">X</span><span class="arrow-a">----&gt;</span><span class="node-y">Y</span><span class="arrow-b">----&gt;</span><span class="node-p">P</span></div>
    <div class="chain-row" style="top:224px"><span class="node-x">X</span><span class="arrow-a">----&gt;</span><span class="node-y">Y</span><span class="arrow-b">----&gt;</span><span class="node-p">P</span></div>
    <div class="chain-row" style="top:336px"><span class="node-x">X</span><span class="arrow-a">----&gt;</span><span class="node-y">Y</span><span class="arrow-b">----&gt;</span><span class="node-p">P</span></div>
    <div class="chain-row" style="top:434px"><span class="node-x">X</span><span class="arrow-a">----&gt;</span><span class="node-y">Y</span><span class="arrow-b">----&gt;</span><span class="node-p">P</span></div>
  </div>

  <footer class="slide-footer"></footer>
  <div class="brand-mark"></div>
  <div class="brand-name">Dellwyn Bluepath</div>
  <div class="social social-chirp"><div class="social-dot"></div><span class="social-handle">@dellwyn</span></div>
  <div class="social social-page"><div class="social-dot"></div><span class="social-handle">/ronandellwyn</span></div>
</div>
</body>
</html>
```